依頼詳細
・B5縦カラー(裏面1c)
・出演アーティストは2組(1.森田ユミ&ルアペドラ、2.吉川沙織&前園剛)で1.がメインアーティストです。
・写真は適宜切り抜きなどしてご使用ください。
・ルアペドラ全員写真+青木カナ1人(写真1,2 いずれか)+ロゴ(適宜着色など)+吉川沙織&前園剛をレイアウトお願いします。

納品時にはSNSなどに使用するバナー画像作成もあわせてお願いいたします。
・コンペでは表面デザインとバナー(横 16:9 )のみお願いします。
決定後裏面に記載する詳細情報をお知らせして仕上げていただきたいと思います。
・バナー画像には詳細テキスト情報は原則として不要です
記載項目
【タイトル】凍てつく宵のフェスタ
【日付】2022年12月16日(金)
【会場名】代官山 ゆうべの窓に灯ともして
渋谷区代官山町14-7
ルミエール代官山B1
【出演者名】
・森田ユミ&ルア・ペドラ
(森田ユミ vocal、杉本健二 sax、大塚理恵 cl、沢井隆史 sax、今野英樹 sax、柳田さえ perc、西川昭夫 bass、川端修平 drums、野口康弘 guitar)
・吉川沙織 vocal & 前園剛 8st-guitar

【時間、料金】
開場 18:30
開演 19:30
前売4000円
当日4500円
(共に+1ドリンク代600円)
サイズ
B5
ページ数
両面
希望イメージ
シンプル 複雑
単色 カラフル
暗い 明るい
日常 高級
遊び心 厳粛
未来的 伝統的
女性的 男性的
希望する色
ライブタイトル、内容にふさわしい色をご提案いただければ幸いです。
納品ファイル
• 高解像度JPG (.jpg)
• イラストレーター形式 (.ai)
• PNG形式 (.png)
補足説明
ルア・ペドラ
ブラジル在住歴22年の森田ユミが日本に帰国後、ブラジルで培ってきた4本サックスがあるラテンコンボを日本で再結成したいと思い出来たのがこのルア・ペドラです。森田ユミのオリジナル曲を中心に、ラテンチックなサウンドにとことん楽しさを追求するコンセプトです。特にライブの後半にはブラジル北東部のカーニバル体験が出来て、思わず心と体が踊り出すことでしょう。

季節感とイベント内容に即したデザインでアーティストにも気に入ってもらえました。

この度は多くのご提案をいただきありがとうございました。
いいデザインが沢山あり絞るのが大変でした。
当選とできなかった皆様にはまた別の機会にお願い出来ればと思っております。
ありがとうございました。

```html
<!DOCTYPE html>
<html lang="ja">
<head>
<meta charset="utf-8">
<title>凍てつく宵のフェスタ</title>
<link href="https://fonts.googleapis.com/css2?family=Shippori+Mincho:wght@500;700&family=Noto+Sans+JP:wght@400;500;700&family=Cormorant+Garamond:ital,wght@0,500;1,500&display=swap" rel="stylesheet">
<style>
:root{
  --sky-top:#3d5f8f;
  --sky-mid:#35406f;
  --night:#2a2350;
  --night-deep:#1d1838;
  --text:#ffffff;
  --soft:#dcd8ee;
  --rule:rgba(255,255,255,.75);
}
*{margin:0;padding:0;box-sizing:border-box}
html,body{width:847px;height:1200px;overflow:hidden;background:var(--night-deep)}
.flyer{position:relative;width:847px;height:1200px;overflow:hidden;color:var(--text);
  font-family:"Noto Sans JP",sans-serif;
  background:linear-gradient(180deg,var(--sky-top) 0%,var(--sky-mid) 40%,var(--night) 65%,var(--night-deep) 100%);}
.backdrop{position:absolute;left:0;top:0;width:847px;height:760px;
  background:radial-gradient(ellipse at 78% 35%,rgba(233,198,184,.32) 0%,rgba(233,198,184,0) 45%),
             radial-gradient(circle at 20% 18%,rgba(255,255,255,.12) 0%,rgba(255,255,255,0) 35%),
             linear-gradient(180deg,rgba(70,100,150,0),rgba(42,35,80,.6) 100%);}
.title{position:absolute;font-family:"Shippori Mincho",serif;font-weight:700;white-space:nowrap;text-shadow:0 0 18px rgba(255,255,255,.35)}
.title-1{top:40px;left:50px;font-size:104px;letter-spacing:4px}
.title-2{top:180px;left:300px;font-size:100px;letter-spacing:4px}
.tagline{position:absolute;right:30px;top:490px;text-align:right;font-size:18px;line-height:2;color:var(--soft)}
.date{position:absolute;left:30px;top:575px;white-space:nowrap;font-family:"Cormorant Garamond",serif}
.date .year{display:block;font-size:36px;margin-left:20px;line-height:1}
.date .big{font-size:118px;font-style:italic;line-height:1}
.date .unit{font-family:"Shippori Mincho",serif;font-size:46px}
.date .day{font-size:30px}
.date .time{font-family:"Shippori Mincho",serif;font-size:34px;font-weight:700;margin-left:12px}
.venue{position:absolute;left:0;width:100%;top:722px;text-align:center;font-size:15px;white-space:nowrap}
.venue span{margin:0 8px}
.cast-head{position:absolute;left:40px;right:40px;top:752px;display:flex;align-items:center;gap:18px;font-size:22px;font-weight:700}
.cast-head::before,.cast-head::after{content:"";flex:1;height:1px;background:var(--rule)}
.photo{position:absolute}
.logo{left:40px;top:792px;width:130px;height:70px;display:flex;align-items:center;justify-content:center;gap:6px;font-size:20px;font-weight:700;white-space:nowrap}
.logo i{width:10px;height:10px;border-radius:50%;background:var(--text);display:block}
.ph-band{left:40px;top:868px;width:170px;height:110px;background:linear-gradient(135deg,#a87c5e,#6b4a3c)}
.ph-kana{left:215px;top:840px;width:155px;height:138px;background:linear-gradient(135deg,#3a2c2c,#8b6a5a)}
.ph-saori{left:425px;top:830px;width:155px;height:148px;background:linear-gradient(135deg,#d9d4d4,#8e8690)}
.ph-tsuyoshi{left:605px;top:820px;width:200px;height:158px;background:linear-gradient(135deg,#2d3e66,#6a5f7a)}
.act{position:absolute;top:986px;font-size:18px;font-weight:700;white-space:nowrap}
.act-main{left:40px}
.act-guest{left:425px}
.members{position:absolute;left:40px;top:1018px;font-size:13px;line-height:1.72}
.members dt{display:inline-block;width:62px}
.members dd{display:inline}
.tickets{position:absolute;left:425px;top:1040px;width:385px}
.tickets h3{display:flex;align-items:center;gap:10px;font-family:"Cormorant Garamond",serif;font-weight:500;font-size:34px;white-space:nowrap}
.tickets h3::before{content:"";width:40px;height:1px;background:var(--rule)}
.tickets .price{margin-top:12px;font-size:15px;text-align:right;white-space:nowrap}
.tickets .foot{margin-top:14px;display:flex;justify-content:space-between;align-items:baseline;white-space:nowrap}
.tickets .note{font-size:11px;color:var(--soft)}
.tickets .tel{font-size:23px;font-weight:700;letter-spacing:1px}
</style>
</head>
<body>
<main class="flyer">
  <div class="backdrop" role="img" aria-label="夜空に浮かぶ観覧車と街の灯りのぼけた光"></div>
  <h1>
    <span class="title title-1">凍てつく宵の</span>
    <span class="title title-2">フェスタ</span>
  </h1>
  <p class="tagline">本格的なブラジル音楽を体感できる<br>とっておきの一夜・・・</p>
  <p class="date"><span class="year">2022年</span><span class="big">12</span><span class="unit">月</span><span class="big">16</span><span class="unit">日</span><span class="day">(金)</span><span class="time">開場 18:30 / 開演 19:30</span></p>
  <p class="venue"><span>会場：代官山 ゆうべの窓に灯ともして</span><span>渋谷区代官山町14-7 ルミエール代官山B1</span></p>
  <h2 class="cast-head">出演者</h2>
  <div class="photo logo"><i></i>Lua Pedra</div>
  <div class="photo ph-band" role="img" aria-label="ルア・ペドラのメンバー集合写真"></div>
  <div class="photo ph-kana" role="img" aria-label="歌う森田ユミの写真"></div>
  <div class="photo ph-saori" role="img" aria-label="吉川沙織の写真"></div>
  <div class="photo ph-tsuyoshi" role="img" aria-label="ギターを持つ前園剛の写真"></div>
  <p class="act act-main">◆ 森田ユミ&amp;ルア・ペドラ</p>
  <p class="act act-guest">◆ 吉川沙織 vocal &amp; 前園剛 8st-guitar</p>
  <dl class="members">
    <div><dt>vocal :</dt><dd>森田ユミ</dd></div>
    <div><dt>sax :</dt><dd>杉本健二・沢井隆史・今野英樹</dd></div>
    <div><dt>cl :</dt><dd>大塚理恵</dd></div>
    <div><dt>perc :</dt><dd>柳田さえ</dd></div>
    <div><dt>bass :</dt><dd>西川昭夫</dd></div>
    <div><dt>drums :</dt><dd>川端修平</dd></div>
    <div><dt>guitar :</dt><dd>野口康弘</dd></div>
  </dl>
  <section class="tickets">
    <h3>ticket information</h3>
    <p class="price">前売 ¥4,000 当日 ¥4,500 (共に＋1ドリンク代 ¥600)</p>
    <div class="foot">
      <p class="note">詳しくはお問い合わせ下さい</p>
      <p class="tel">TEL : 000-000-0000</p>
    </div>
  </section>
</main>
</body>
</html>
```